Veloran Dental Development - Business Cards

We are a Dental Development and Management company. We are looking to develop a new business card design. We are business professional but modern. The logo that I have attached is the business colors. You can also check out our website for further detail. www.veloranmgmt-example.com

Target Market(s)

Dental Professionals, Dentists and Office Staff, Marketing Professionals

Industry/Entity Type

Business

Requirements
Must have
• Name - Bartholomew K. Tressing
Title - Marketing Director
Phone - 555-019-4827
Cell - 555-019-4827
Email - Bart.t@veloran-example.com
Address - 2917 W Larkmoor Rd, Mesa, AZ 85209
Web- www.veloran-example.com

Veloran Logo must go on the front. The other logos go on the back as affiliated businesses

Must be editable to enter specific Names, Positions, Phone numbers and email later on. Using Adobe CS5 currently.

```html
<!DOCTYPE html>
<html lang="en">
<head>
<meta charset="utf-8">
<title>Veloran Dental Development – Business Cards</title>
<link rel="stylesheet" href="https://fonts.googleapis.com/css2?family=Source+Sans+3:wght@400;600;700&display=swap">
<style>
  :root{
    --navy:#262a6b;
    --taupe:#a39884;
    --taupe-dark:#978b74;
    --gold:#e39a2b;
    --white:#ffffff;
    --backdrop:#ece8e1;
    --ink:#262a6b;
  }
  *{box-sizing:border-box;margin:0;padding:0}
  html,body{width:1200px;height:1000px;overflow:hidden}
  body{
    background:var(--backdrop);
    font-family:"Source Sans 3",Arial,sans-serif;
    color:var(--ink);
    position:relative;
  }
  .card{
    position:absolute;
    left:240px;
    width:720px;
    height:410px;
    border-radius:20px;
    background:var(--white);
    overflow:hidden;
    box-shadow:0 6px 18px rgba(60,50,30,.25);
  }
  .card--front{top:55px}
  .card--back{top:530px}
  .edge-strip{
    position:absolute;left:0;top:0;bottom:0;width:18px;
    display:flex;flex-direction:column;
  }
  .edge-strip span{flex:1}
  .edge-strip .navy{background:var(--navy)}
  .edge-strip .taupe{background:var(--taupe)}
  .edge-strip .gold{background:var(--gold)}

  .brand-name{
    display:flex;align-items:center;gap:12px;
    font-weight:700;color:var(--navy);
    letter-spacing:.5px;
  }
  .brand-name .dot{
    width:26px;height:26px;border-radius:50%;
    background:var(--gold);flex:none;
  }
  .card--front .brand-name{position:absolute;left:52px;top:62px;font-size:26px;line-height:1.1;width:300px}

  .contact-panel{
    position:absolute;right:0;top:0;bottom:0;width:420px;
    background:linear-gradient(90deg,var(--white) 0%,#e9e5dd 30%,var(--taupe) 100%);
  }
  .contact-block{
    position:absolute;right:30px;top:22px;height:366px;
    writing-mode:vertical-rl;
    transform:rotate(180deg);
    display:flex;flex-direction:column;gap:0;
  }
  .person-name{font-size:27px;font-weight:700;color:var(--navy);line-height:1.25}
  .person-title{font-size:21px;font-weight:400;color:var(--navy);line-height:1.2;margin-left:34px}
  .contact-line{
    display:flex;align-items:center;gap:10px;
    font-size:16px;color:var(--navy);line-height:1.9;
  }
  .contact-line svg{width:15px;height:15px;flex:none;transform:rotate(90deg)}

  .card--back .brand-name{
    position:absolute;left:0;right:0;top:120px;
    justify-content:center;font-size:34px;
  }
  .affiliates{
    position:absolute;left:40px;right:24px;top:300px;
    display:flex;justify-content:space-around;align-items:center;
  }
  .affiliate{
    font-size:16px;font-weight:600;text-align:center;line-height:1.15;
    display:flex;align-items:center;gap:8px;
  }
  .affiliate .mark{width:16px;height:16px;flex:none}
  .affiliate--plan{color:#b8312f}
  .affiliate--plan .mark{background:#b8312f;border-radius:50%}
  .affiliate--centers{color:#2f5f9a}
  .affiliate--centers .mark{background:#2f5f9a;border-radius:50%}
  .affiliate--rapid{color:#d1202a}
  .affiliate--rapid .mark{background:#d1202a}
  .affiliate--kids{color:#8a2c8f}
  .affiliate--kids .mark{background:#f2c12e;border-radius:50%}
</style>
</head>
<body>

<section class="card card--front" aria-label="Business card front">
  <div class="edge-strip"><span class="navy"></span><span class="taupe"></span><span class="gold"></span></div>
  <div class="brand-name"><span class="dot"></span><span>Veloran Dental Development</span></div>
  <div class="contact-panel">
    <div class="contact-block">
      <div class="person-name">Bartholomew K. Tressing</div>
      <div class="person-title">Marketing Director</div>
      <div class="contact-line">
        <svg viewBox="0 0 16 16"><rect x="1" y="3" width="14" height="11" rx="1" fill="var(--navy)"/><rect x="3" y="5" width="10" height="3" fill="#fff"/></svg>
        <span>555-019-4827</span>
      </div>
      <div class="contact-line">
        <svg viewBox="0 0 16 16"><rect x="4" y="1" width="8" height="14" rx="1.5" fill="var(--navy)"/><rect x="5.5" y="3" width="5" height="7" fill="#fff"/></svg>
        <span>555-019-4827</span>
      </div>
      <div class="contact-line">
        <svg viewBox="0 0 16 16"><rect x="1" y="3" width="14" height="10" fill="var(--navy)"/><path d="M1 3 L8 9 L15 3" stroke="#fff" stroke-width="1.3" fill="none"/></svg>
        <span>Bart.t@veloran-example.com</span>
      </div>
      <div class="contact-line">
        <svg viewBox="0 0 16 16"><path d="M8 1 L15 8 L12 8 L12 15 L4 15 L4 8 L1 8 Z" fill="var(--navy)"/></svg>
        <span>2917 W Larkmoor Rd, Mesa, AZ 85209</span>
      </div>
      <div class="contact-line">
        <svg viewBox="0 0 16 16"><circle cx="8" cy="8" r="7" fill="var(--navy)"/><path d="M1 8 H15 M8 1 V15 M3 4 Q8 6 13 4 M3 12 Q8 10 13 12" stroke="#fff" stroke-width="1" fill="none"/></svg>
        <span>www.veloran-example.com</span>
      </div>
    </div>
  </div>
</section>

<section class="card card--back" aria-label="Business card back">
  <div class="edge-strip"><span class="navy"></span><span class="taupe"></span><span class="gold"></span></div>
  <div class="brand-name"><span class="dot"></span><span>Veloran Dental Development</span></div>
  <div class="affiliates">
    <div class="affiliate affiliate--plan"><span class="mark"></span><span>Hearthside<br>Dental Plan</span></div>
    <div class="affiliate affiliate--centers"><span class="mark"></span><span>Hearthside<br>Dental Centers</span></div>
    <div class="affiliate affiliate--rapid"><span class="mark"></span><span>Rapidcare<br>Dental Centers</span></div>
    <div class="affiliate affiliate--kids"><span class="mark"></span><span>Brightsmile<br>Kids</span></div>
  </div>
</section>

</body>
</html>
```